Roll label Flyer design

I need a flyer for a roll label printer
Pictures for the project are located here:
https://plimtonstickers.sharefile.com/d-k4wq7812m3a0z551

Text I want is located here:
https://plimtonstickers.com/roll-labels.php

Target Market(s)

Manufactures, wholesalers

Industry/Entity Type

Printing

Requirements
Must have
• Lots of pictures. Our phone number 800-472-8164. Website www.plimtonstickers.com

```html
<!DOCTYPE html>
<html lang="en">
<head>
<meta charset="utf-8">
<title>Roll Label Printer – Plimton Stickers</title>
<link rel="stylesheet" href="https://fonts.googleapis.com/css2?family=Exo+2:wght@700;800&family=Saira:wght@400;500&display=swap">
<style>
  :root {
    --red: #c3161c;
    --red-deep: #a90f14;
    --charcoal: #2e2f32;
    --slate: #4a4b4e;
    --tag-grey: #4b4c4f;
    --footer-dark: #1f1f20;
    --white: #ffffff;
    --soft: #e9e9ea;
  }
  * { box-sizing: border-box; margin: 0; padding: 0; }
  html, body { width: 928px; height: 1200px; overflow: hidden; background: var(--slate); }
  .flyer {
    position: relative; width: 928px; height: 1200px; overflow: hidden;
    background: var(--slate); font-family: "Saira", sans-serif; color: var(--white);
  }
  .header {
    position: absolute; left: 0; top: 0; width: 928px; height: 144px;
    background: linear-gradient(180deg, #36373a 0%, #2a2b2e 100%);
    border-bottom: 3px solid var(--white);
  }
  .brand {
    position: absolute; right: 42px; top: 44px; display: flex; align-items: center; gap: 14px;
  }
  .brand-dot { width: 52px; height: 52px; border-radius: 50%; background: var(--red); }
  .brand-name {
    font-family: "Saira", sans-serif; font-weight: 500; font-size: 30px;
    letter-spacing: 7px; text-transform: uppercase; color: var(--white);
  }
  .hero-photo {
    position: absolute; left: 0; top: 147px; width: 928px; height: 533px;
    background: radial-gradient(ellipse at 55% 40%, #9a9ea3 0%, #6c7075 45%, #3f4245 100%);
  }
  .corner-flag { position: absolute; left: 0; top: 0; width: 370px; height: 380px; }
  .corner-mark {
    position: absolute; left: 48px; top: 50px; width: 84px; height: 84px;
    border-radius: 50%; background: var(--white);
  }
  .intro-box {
    position: absolute; left: 98px; top: 316px; width: 261px; height: 350px;
    background: var(--red); padding: 34px 26px 0 26px;
  }
  .intro-box h2 {
    font-family: "Exo 2", sans-serif; font-weight: 800; font-size: 20px; margin-bottom: 10px;
  }
  .intro-box p {
    font-size: 16px; line-height: 22.4px; letter-spacing: 1.6px; text-align: justify;
  }
  .features { position: absolute; right: 58px; top: 244px; text-align: right; }
  .features h3 {
    font-family: "Exo 2", sans-serif; font-weight: 800; font-size: 27px; margin-bottom: 10px;
  }
  .feature-tag {
    display: block; margin-left: auto; width: max-content; height: 33px; line-height: 33px;
    padding: 0 8px 0 14px; font-size: 21px; margin-bottom: 22px;
  }
  .feature-tag.red { background: var(--red); }
  .feature-tag.grey { background: var(--tag-grey); }
  .gallery { position: absolute; left: 0; top: 620px; width: 928px; height: 260px; }
  .snap {
    position: absolute; border: 6px solid var(--white);
    box-shadow: 0 6px 14px rgba(0,0,0,0.45);
  }
  .markets-title {
    position: absolute; left: 0; top: 900px; width: 928px; text-align: center;
    font-family: "Exo 2", sans-serif; font-weight: 800; font-size: 23px; letter-spacing: 0.4px;
  }
  .market { position: absolute; top: 952px; width: 140px; text-align: center; }
  .market-icon {
    width: 92px; height: 92px; border-radius: 50%; margin: 0 auto;
    background: var(--red); border: 3px solid var(--white);
    display: flex; align-items: center; justify-content: center;
  }
  .market-name { margin-top: 18px; font-size: 15.5px; line-height: 19px; color: var(--soft); }
  .footer { position: absolute; left: 0; top: 1108px; width: 928px; height: 92px; }
  .footer-phone {
    position: absolute; left: 0; top: 0; width: 464px; height: 92px; background: var(--footer-dark);
    display: flex; align-items: center; justify-content: center; gap: 14px;
    font-family: "Exo 2", sans-serif; font-weight: 800; font-size: 37px; letter-spacing: 1px;
  }
  .footer-web {
    position: absolute; left: 464px; top: 0; width: 464px; height: 92px; background: var(--red);
    display: flex; align-items: center; justify-content: center; gap: 10px;
    font-family: "Exo 2", sans-serif; font-weight: 800; font-size: 22px;
  }
</style>
</head>
<body>
<div class="flyer">
  <div class="header">
    <div class="brand"><span class="brand-dot"></span><span class="brand-name">Plimton Stickers</span></div>
  </div>

  <div class="hero-photo" role="img" aria-label="Photo of the roll label printing press on the production floor"></div>

  <svg class="corner-flag" viewBox="0 0 370 380" aria-hidden="false">
    <polygon points="0,0 362,0 0,372" fill="var(--red)"/>
    <text x="0" y="0" transform="translate(52,316) rotate(-45)" fill="#fff"
      font-family="'Exo 2', sans-serif" font-weight="800" font-size="30" letter-spacing="1">ROLL LABEL PRINTER</text>
  </svg>
  <div class="corner-mark"></div>

  <section class="intro-box">
    <h2>Roll/Product Labels</h2>
    <p>Long or short run. Digital or flexographic. Standard shapes or unique, custom diecuts. Simple spot colors or full color with every embellishment. Let us help you create the perfect label for your application.</p>
  </section>

  <section class="features">
    <h3>Features:</h3>
    <span class="feature-tag red">Embossing</span>
    <span class="feature-tag grey">Foil-Stamping</span>
    <span class="feature-tag red">Spot Varnishes</span>
    <span class="feature-tag grey">Instant Redeemable Coupons</span>
    <span class="feature-tag red">Expanded Content/Booklet Labels</span>
  </section>

  <div class="gallery">
    <div class="snap" role="img" aria-label="Close-up of printed product labels on a roll"
      style="left:-10px; top:55px; width:230px; height:170px; transform:rotate(-8deg); background:linear-gradient(135deg,#7a6a4e,#d9d2c4 55%,#3b3b3b);"></div>
    <div class="snap" role="img" aria-label="Blue labels running through the press rollers"
      style="left:186px; top:60px; width:210px; height:175px; transform:rotate(-6deg); background:linear-gradient(90deg,#cfd0d2,#6e7275 45%,#2f73b5 70%,#d8d8d8);"></div>
    <div class="snap" role="img" aria-label="White labels with green stripe on the press web"
      style="left:368px; top:72px; width:214px; height:160px; transform:rotate(-7deg); background:linear-gradient(160deg,#5c5e60,#e6e6e6 50%,#2a2b2c);"></div>
    <div class="snap" role="img" aria-label="Red danger warning labels on a roll"
      style="left:548px; top:60px; width:238px; height:178px; transform:rotate(4deg); background:linear-gradient(120deg,#3a3a3a,#7d7d7d 40%,#c9282c 70%,#e8e8e8);"></div>
    <div class="snap" role="img" aria-label="Roll of finished dark product labels on a spindle"
      style="left:682px; top:12px; width:250px; height:180px; transform:rotate(6deg); background:linear-gradient(100deg,#f0f0f0 10%,#27292e 40%,#4a4e57 70%,#9aa0a6);"></div>
  </div>

  <h2 class="markets-title">Specialty Markets We Service Include:</h2>

  <div class="market" style="left:56px;">
    <div class="market-icon">
      <svg width="50" height="50" viewBox="0 0 50 50" fill="#fff"><path d="M6 4h14l-2 30a5 5 0 0 1-10 0z"/><rect x="26" y="20" width="6" height="6"/><rect x="22" y="26" width="22" height="20" rx="3"/><circle cx="33" cy="36" r="4" fill="var(--red)"/></svg>
    </div>
    <div class="market-name">Health &amp; Beauty</div>
  </div>
  <div class="market" style="left:192px;">
    <div class="market-icon">
      <svg width="50" height="50" viewBox="0 0 50 50" fill="none" stroke="#fff" stroke-width="5" stroke-linecap="round"><path d="M8 42L30 20"/><ellipse cx="35" cy="14" rx="7" ry="9" transform="rotate(45 35 14)" fill="#fff" stroke="none"/><path d="M42 42L14 14"/><path d="M8 8l10 10M14 4l8 8M4 14l8 8"/></svg>
    </div>
    <div class="market-name">Food &amp; Beverage</div>
  </div>
  <div class="market" style="left:328px;">
    <div class="market-icon">
      <svg width="50" height="54" viewBox="0 0 50 54" fill="none" stroke="#fff" stroke-width="3"><path d="M4 18h16c0 10-4 14-8 14s-8-4-8-14zM12 32v14M6 46h12"/><path d="M34 2h6v10l4 6v34H30V18l4-6z" fill="#fff" stroke="none"/><rect x="32" y="26" width="10" height="12" fill="var(--red)"/></svg>
    </div>
    <div class="market-name">Wine &amp; Spirits</div>
  </div>
  <div class="market" style="left:464px;">
    <div class="market-icon">
      <svg width="60" height="52" viewBox="0 0 60 52" fill="#fff"><path d="M16 22a14 14 0 0 1 28 0h4v5H12v-5z"/><path d="M2 24l8 14 14 8v6H12L2 40zM58 24l-8 14-14 8v6h12l10-12z"/></svg>
    </div>
    <div class="market-name">Industrial Safety<br>&amp; Warning</div>
  </div>
  <div class="market" style="left:600px;">
    <div class="market-icon">
      <svg width="50" height="50" viewBox="0 0 50 50" fill="none" stroke="#fff" stroke-width="4"><rect x="8" y="8" width="34" height="26" rx="2"/><path d="M25 34v8M16 44h18"/><path d="M16 18h6l10-6v18l-10-6h-6z" fill="#fff"/></svg>
    </div>
    <div class="market-name">Promotional</div>
  </div>
  <div class="market" style="left:738px;">
    <div class="market-icon">
      <svg width="50" height="54" viewBox="0 0 50 54" fill="none" stroke="#fff" stroke-width="3"><rect x="8" y="4" width="30" height="40" rx="2"/><path d="M14 14h18M14 21h18M14 28h12"/><circle cx="36" cy="40" r="10" fill="var(--red)"/><path d="M31 40l4 4 7-7"/></svg>
    </div>
    <div class="market-name">Compliance</div>
  </div>

  <footer class="footer">
    <div class="footer-phone">
      <svg width="32" height="32" viewBox="0 0 24 24" fill="#fff"><path d="M6.6 10.8a15 15 0 0 0 6.6 6.6l2.2-2.2a1 1 0 0 1 1-.25 11.4 11.4 0 0 0 3.6.57 1 1 0 0 1 1 1V20a1 1 0 0 1-1 1A17 17 0 0 1 3 4a1 1 0 0 1 1-1h3.5a1 1 0 0 1 1 1c0 1.25.2 2.45.57 3.57a1 1 0 0 1-.25 1z"/></svg>
      <span>800-472-8164</span>
    </div>
    <div class="footer-web">
      <svg width="30" height="30" viewBox="0 0 30 30" fill="none" stroke="#fff" stroke-width="2.5"><circle cx="11" cy="11" r="8"/><path d="M13 13l4 14 3-5 5 5 2-2-5-5 5-3z" fill="#fff"/></svg>
      <span>Website www.plimtonstickers.com</span>
    </div>
  </footer>
</div>
</body>
</html>
```